Brochure 11 x 25.5 Trifold

Brightlane Staffworks, Inc. is a payroll, benefits, and HR administration company. We are in need of a brochure to showcase all of our services. Attached is a one-page information sheet that contains the information we want in the brochure as well as several images. The brochure is a 11 x 25.5 tri-fold (a sample is attached). Please use the colors in the attached logo and design to complement our website brightlanestaff.example.
Target Market(s)
Company executives
Industry/Entity Type
Human Resource Management
Font styles to use
Other font styles liked:
- Avenir LT
Colors
Designer to choose colors to be used in the design.
Look and feel
Each slider illustrates characteristics of the customer's brand and the style your logo design should communicate.

```html
<!DOCTYPE html>
<html lang="en">
<head>
<meta charset="utf-8">
<title>Brightlane Staffworks – Trifold Brochure</title>
<link href="https://fonts.googleapis.com/css2?family=Nunito+Sans:wght@300;400;600&display=swap" rel="stylesheet">
<style>
:root{
  --green:#8aa63a;
  --navy:#0d3a5c;
  --ink:#2f3a40;
  --paper:#f2f2f2;
  --paper-dark:#d9dadb;
  --stage:#939b99;
  --photo-warm:#c9b8a6;
  --photo-cool:#a9b4bd;
}
*{margin:0;padding:0;box-sizing:border-box}
html,body{width:1200px;height:1200px;overflow:hidden}
body{background:var(--stage);font-family:"Nunito Sans",Arial,sans-serif;color:var(--ink);font-weight:300}
.canvas{position:relative;width:1200px;height:1200px;background:linear-gradient(180deg,#8f9896,#a0a7a5 60%,#8c9593)}
.spread{position:absolute;overflow:hidden;box-shadow:0 6px 14px rgba(0,0,0,.35);background:linear-gradient(90deg,#e9eaea,#f7f7f7 40%,#e4e5e5)}
.spread--outside{left:50px;top:96px;width:1088px;height:469px}
.spread--inside{left:50px;top:612px;width:1099px;height:473px}
.spread svg.shapes{position:absolute;left:0;top:0}
.t{position:absolute;line-height:1.15}
.h-section{font-size:18px;color:var(--navy);font-weight:300;letter-spacing:.3px}
.about h1{font-size:18px;font-weight:300;color:var(--ink)}
.about h2{font-size:6.5px;font-weight:400;margin:10px 0 4px}
.about p{font-size:5.2px;line-height:7px;margin-bottom:6px}
.cycle-label{font-size:10px;font-weight:300}
.cycle-desc{font-size:5.2px;line-height:7px;width:60px;margin-top:3px}
.green{color:var(--green)}
.navy{color:var(--navy)}
.brand{font-size:10px;color:var(--navy);font-weight:400;display:flex;align-items:center;gap:5px;letter-spacing:.3px;white-space:nowrap}
.brand i{display:inline-block;width:9px;height:9px;border-radius:50%;background:var(--green)}
.brand--compact{font-size:9px;letter-spacing:0;gap:4px}
.contact{font-size:6.2px;text-align:center;width:120px}
.contact div{margin-bottom:8px}
.contact svg{display:block;margin:0 auto 2px}
.hero{font-size:18px;color:#e8eef2;font-weight:300;line-height:23px}
.hero b{display:block;color:var(--green);font-weight:300;font-size:25px;line-height:30px;margin-top:2px}
.svc-title{font-size:10px;color:var(--ink);font-weight:300;width:120px;line-height:12px}
.svc ul{list-style:none;margin-top:3px}
.svc li{font-size:5.2px;line-height:7px;padding-left:10px;position:relative;width:120px}
.svc li::before{content:"";position:absolute;left:1px;top:2px;width:4px;height:3px;background:var(--navy);border-radius:0 2px 0 2px;transform:skewX(-20deg)}
.icon{position:absolute;width:32px;height:32px;border-radius:4px;background:var(--navy)}
.icon svg{width:32px;height:32px}
.perk-icon{position:absolute;width:32px;height:32px;background:var(--green);border-radius:2px}
.perk-icon svg{width:32px;height:32px}
.perk{font-size:5.2px;line-height:6.6px;width:95px}
.cover-head{font-size:15px;color:var(--navy);font-weight:300;line-height:17px}
.cover-copy{font-size:6.8px;line-height:8.5px;width:150px}
.pill{background:var(--green);color:var(--navy);font-size:8.5px;line-height:9.5px;padding:2px 6px;border-radius:0 8px 8px 0;width:145px}
</style>
</head>
<body>
<div class="canvas">

  <section class="spread spread--outside">
    <svg class="shapes" width="1088" height="469" viewBox="0 0 1088 469">
      <defs>
        <linearGradient id="warmPhoto" x1="0" y1="0" x2="1" y2="1">
          <stop offset="0" stop-color="#e8e4df"/><stop offset=".5" stop-color="#c9b8a6"/><stop offset="1" stop-color="#8c7a6c"/>
        </linearGradient>
        <linearGradient id="officePhoto" x1="0" y1="0" x2="1" y2="1">
          <stop offset="0" stop-color="#e3e6e8"/><stop offset=".5" stop-color="#9aa3aa"/><stop offset="1" stop-color="#4c5560"/>
        </linearGradient>
      </defs>
      <path d="M0 0H531L375 272Q360 296 330 286H0Z" fill="var(--green)"/>
      <path d="M535 0H553L434 158H418Z" fill="var(--navy)"/>
      <g role="img" aria-label="Photo of a smiling woman in glasses working at a laptop">
        <path d="M0 215H262Q305 215 292 258L150 469H0Z" fill="url(#warmPhoto)"/>
      </g>
      <path d="M300 225Q318 250 300 280L170 469" stroke="var(--green)" stroke-width="2" fill="none"/>
      <path d="M200 469L292 330Q300 318 305 332L305 400L262 469Z" fill="var(--navy)"/>
      <path d="M522 469L632 350Q645 340 668 344L592 469Z" fill="var(--green)"/>
      <g role="img" aria-label="Photo of a business team meeting around a conference table">
        <path d="M919 0H1088V345H1020L1030 262H758Z" fill="url(#officePhoto)"/>
      </g>
      <path d="M940 0H956L805 170H789Z" fill="var(--green)"/>
      <path d="M975 0L760 262" stroke="var(--navy)" stroke-width="2"/>
      <path d="M552 469L700 264Q712 248 740 248H1000Q1030 250 1012 292L937 469Z" fill="var(--navy)"/>
      <path d="M1008 372Q1030 380 1060 360L1088 320" stroke="var(--navy)" stroke-width="2.5" fill="none"/>
      <path d="M937 469H1088V425H972Z" fill="var(--green)"/>
      <g fill="none" stroke-width="1.3">
        <path d="M587 154A45 45 0 0 1 630 184" stroke="var(--navy)"/>
        <path d="M632 210A45 45 0 0 1 595 243" stroke="var(--navy)"/>
        <path d="M572 242A45 45 0 0 1 542 200" stroke="var(--navy)"/>
        <path d="M544 185A45 45 0 0 1 575 156" stroke="var(--navy)"/>
        <path d="M562 166A37 37 0 0 1 612 166" stroke="var(--green)"/>
        <path d="M622 205A37 37 0 0 1 600 233" stroke="var(--green)"/>
        <path d="M565 228A37 37 0 0 1 552 188" stroke="var(--green)"/>
        <path d="M587 130V146M628 152L641 144M628 246L641 254M587 252V268M546 246L533 254M546 152L533 144" stroke="var(--navy)"/>
        <path d="M626 180L630 186L634 179M597 240L591 243L597 247M546 204L542 198L538 204" stroke="var(--navy)"/>
        <path d="M608 162L613 166L607 169M604 229L599 234L606 235M549 193L552 187L556 193" stroke="var(--green)"/>
      </g>
      <line x1="363" y1="0" x2="363" y2="469" stroke="rgba(0,0,0,.08)"/>
      <line x1="726" y1="0" x2="726" y2="469" stroke="rgba(0,0,0,.08)"/>
    </svg>

    <div class="t about" style="left:34px;top:28px;width:305px">
      <h1>ABOUT US</h1>
      <h2>ABOUT BSW HUMAN CAPITAL MANAGEMENT SERVICES</h2>
      <p>Brightlane Staffworks has been providing companies with human capital management solutions since 1996. BSW was started by Tom Hale, an entrepreneur with a strong business background and a history of working with numerous service providers. Tom saw the need for quality HR and payroll regulatory solutions. While Tom is now retired, his passion and vision is carried on by his daughter-in-law Dana Hale. Dana started working with BSW at its inception while still in college. She has now worked in every aspect of the business and consulted with hundreds of clients over the years.</p>
      <p>While Tom was a pioneer in the HR outsourcing industry in the 1990's, today Dana is leading the way as a new pioneer, ushering in the latest innovations to the industry. As compliance becomes standardized, her passion, and the new frontier of HR, is to help businesses recognize the distinct strategic advantages to having strong organizational health and providing a great employee experience.</p>
    </div>

    <div class="t" style="left:559px;top:80px"><div class="cycle-label green">ONBOARDING</div><div class="cycle-desc">Auto generate notice to new-hire, standard and customized forms and acknowledgements</div></div>
    <div class="t" style="left:651px;top:134px"><div class="cycle-label navy">PAYROLL</div><div class="cycle-desc">HRIS, Direct deposits, New Hire Reporting, Employee Portal, Year End Reporting</div></div>
    <div class="t" style="left:651px;top:200px"><div class="cycle-label green">BENEFITS</div><div class="cycle-desc">Online enrollment, application, benefit reconciliations, eligibility tracking notifications, retirement plan</div></div>
    <div class="t" style="left:558px;top:267px"><div class="cycle-label navy">EMPLOYEE<br>MANAGEMENT</div><div class="cycle-desc">Culture development, discipline, leave management, Workers' Compensation claims, employee verifications, handbook</div></div>
    <div class="t" style="left:466px;top:229px"><div class="cycle-label green">SEPARATION</div><div class="cycle-desc">COBRA, Retirement plan assistance, DOL Notices</div></div>
    <div class="t" style="left:466px;top:146px"><div class="cycle-label navy">HIRING</div><div class="cycle-desc">Integrated cloud-based ATS, Auto post to job boards, applicant management and screening</div></div>
    <div class="t" style="left:557px;top:187px;width:60px;text-align:center;font-size:10px;line-height:11px"><span class="navy">EMPLOYEE</span><br><span class="green">LIFECYCLE</span></div>

    <div class="t brand" style="left:388px;top:333px"><i></i>BRIGHTLANE STAFFWORKS</div>
    <div class="t contact" style="left:382px;top:365px">
      <div><svg width="7" height="8" viewBox="0 0 7 8"><path d="M3.5 8L1 4A2.5 2.5 0 1 1 6 4Z" fill="var(--navy)"/><circle cx="3.5" cy="2.8" r="1" fill="#fff"/></svg>1420 Larkfield Road<br>Riverton, LA 70000</div>
      <div><svg width="7" height="7" viewBox="0 0 7 7"><path d="M1 1L2.5 .5 3.3 2.3 2.3 3A4 4 0 0 0 4 4.7L4.7 3.7 6.5 4.5 6 6Q2 6 1 1Z" fill="var(--navy)"/></svg>555-014-2200</div>
      <div><svg width="7" height="6" viewBox="0 0 7 6"><rect x=".5" y=".5" width="6" height="5" fill="var(--navy)"/><path d="M.5 .5L3.5 3 6.5 .5" stroke="#fff" stroke-width=".6" fill="none"/></svg>info@brightlanestaff.example</div>
      <div><svg width="7" height="7" viewBox="0 0 7 7"><circle cx="3.5" cy="3.5" r="3" fill="none" stroke="var(--navy)"/><path d="M.5 3.5H6.5M3.5 .5V6.5" stroke="var(--navy)" stroke-width=".6"/></svg>www.brightlanestaff.example</div>
    </div>

    <div class="t brand" style="left:737px;top:16px"><i></i>BRIGHTLANE STAFFWORKS</div>
    <div class="t hero" style="left:751px;top:290px">Your single-source<br>solution for the<b>ENTIRE<br>EMPLOYEE<br>LIFECYCLE</b></div>
  </section>

  <section class="spread spread--inside">
    <svg class="shapes" width="1099" height="473" viewBox="0 0 1099 473">
      <defs>
        <linearGradient id="teamPhoto" x1="0" y1="0" x2="1" y2="1">
          <stop offset="0" stop-color="#dfe1e3"/><stop offset=".45" stop-color="#b9b3ae"/><stop offset="1" stop-color="#6e7276"/>
        </linearGradient>
        <linearGradient id="deskPhoto" x1="0" y1="0" x2="1" y2="1">
          <stop offset="0" stop-color="#eef0f1"/><stop offset=".5" stop-color="#c7c2bb"/><stop offset="1" stop-color="#7d6a5c"/>
        </linearGradient>
      </defs>
      <g role="img" aria-label="Overhead photo of four colleagues reviewing papers at a glass table">
        <path d="M0 0H366V55L242 264Q232 280 212 280H0Z" fill="url(#teamPhoto)"/>
        <path d="M366 0H410L366 70Z" fill="url(#teamPhoto)"/>
      </g>
      <g role="img" aria-label="Laptop and phone showing the online employee portal">
        <rect x="192" y="370" width="124" height="80" rx="3" fill="#2b2f33"/>
        <rect x="196" y="374" width="116" height="70" fill="#e9ecee"/>
        <rect x="310" y="395" width="33" height="60" rx="4" fill="#2b2f33"/>
        <rect x="312" y="400" width="29" height="50" fill="#dfe3e6"/>
      </g>
      <g role="img" aria-label="Photo of two women talking across a desk in a bright office">
        <path d="M742 473V340Q742 288 790 288H1060Q1099 288 1099 330V473Z" fill="url(#deskPhoto)"/>
      </g>
      <path d="M760 473L770 340Q776 302 815 302H1050Q1085 305 1078 345L1020 473" stroke="var(--navy)" stroke-width="2" fill="none"/>
      <path d="M742 473V380L790 330H802L752 473Z" fill="var(--green)"/>
      <path d="M1000 473L1099 410V473Z" fill="var(--green)"/>
      <line x1="366" y1="0" x2="366" y2="473" stroke="rgba(0,0,0,.08)"/>
      <line x1="731" y1="0" x2="731" y2="473" stroke="rgba(0,0,0,.08)"/>
    </svg>

    <div class="t cover-head" style="left:30px;top:310px">FROM HIRE TO<br>RETIRE, WE'VE<br>GOT YOU COVERED</div>
    <div class="t cover-copy" style="left:30px;top:363px">Brightlane Staffworks has been delivering quality HR and Payroll services for over 25 years. Our dedicated team of professionals is focused on being the best service provider in the industry. Our goal is to relieve business executives of the challenges of managing a dynamic and growing workforce in today's regulatory environment and give them the freedom to focus on what drives their business.</div>

    <div class="t h-section" style="left:438px;top:22px;font-size:14px">OUR SERVICES</div>

    <div class="icon" style="left:397px;top:87px"><svg viewBox="0 0 32 32"><rect x="7" y="11" width="18" height="10" fill="none" stroke="#fff"/><path d="M10 15H18M10 18H14" stroke="#fff"/></svg></div>
    <div class="t svc" style="left:440px;top:47px"><div class="svc-title">Payroll</div><ul><li>Fast, efficient, accurate</li><li>Paper checks or direct deposit</li><li>Easy time file uploads or integrated time clock options</li><li>New hire reporting</li><li>Custom G/L file</li><li>Comprehensive reporting options</li><li>Certified payroll option</li></ul></div>

    <div class="icon" style="left:561px;top:93px"><svg viewBox="0 0 32 32"><path d="M10 7H19L23 11V25H10Z" fill="none" stroke="#fff"/><path d="M13 14H20M13 17H20M13 20H20" stroke="#fff"/></svg></div>
    <div class="t svc" style="left:598px;top:47px"><div class="svc-title">Employee Onboarding</div><ul><li>Simple, accurate, paperless</li><li>Custom forms and acknowledgements</li><li>Standard forms (W-4, I-9, State withholding, etc)</li><li>Paperless, electronic signatures</li><li>Employee handbook and policy acknowledgements</li><li>Custom welcome videos</li></ul></div>

    <div class="icon" style="left:397px;top:170px"><svg viewBox="0 0 32 32"><rect x="7" y="10" width="18" height="12" rx="1" fill="none" stroke="#fff"/><path d="M7 14H25M10 19H14" stroke="#fff"/></svg></div>
    <div class="t svc" style="left:440px;top:134px"><div class="svc-title">Cafeteria/FSA/HRA Administration</div><ul><li>Plan documents/materials</li><li>Debit cards</li><li>Easy 24/7 online reporting</li><li>Claims processing</li><li>Plan testing</li></ul></div>

    <div class="icon" style="left:561px;top:170px"><svg viewBox="0 0 32 32"><path d="M7 13L16 7 25 13V24H7Z" fill="none" stroke="#fff"/><path d="M7 13L16 19 25 13" stroke="#fff" fill="none"/></svg></div>
    <div class="t svc" style="left:598px;top:134px"><div class="svc-title">COBRA<br>Administration</div><ul><li>Initial notices</li><li>Open enrollment notices</li><li>Easy 24/7 online reporting</li><li>Qualified beneficiary election notices</li><li>Premium collection</li><li>Access to professional advice</li></ul></div>

    <div class="icon" style="left:397px;top:276px"><svg viewBox="0 0 32 32"><path d="M16 24L8 15A4.5 4.5 0 0 1 16 10 4.5 4.5 0 0 1 24 15Z" fill="none" stroke="#fff"/><path d="M9 16H13L15 13 17 19 19 16H23" stroke="#fff" fill="none"/></svg></div>
    <div class="t svc" style="left:440px;top:217px"><div class="svc-title">Benefits<br>Management</div><ul><li>Customized benefits packet</li><li>Track new hire eligibility</li><li>Open enrollment assistance</li><li>Electronic enrollment</li><li>Track and submit enrollments</li><li>Provide 401k census report</li><li>Remit retirement plan reports and funds</li><li>ACA compliance</li></ul></div>

    <div class="icon" style="left:561px;top:276px"><svg viewBox="0 0 32 32"><circle cx="11" cy="13" r="2.5" fill="none" stroke="#fff"/><circle cx="21" cy="13" r="2.5" fill="none" stroke="#fff"/><circle cx="16" cy="17" r="2.5" fill="none" stroke="#fff"/><path d="M7 21Q11 17 14 19M25 21Q21 17 18 19M11 25Q16 19 21 25" fill="none" stroke="#fff"/></svg></div>
    <div class="t svc" style="left:598px;top:217px"><div class="svc-title">Human Resource<br>Administration</div><ul><li>Wage and hour compliance</li><li>Employee handbooks</li><li>Employee discipline and termination consulting</li><li>Performance management</li><li>Workers' comp claims administration</li><li>Unemployment administration</li><li>Manager training</li></ul></div>

    <div class="icon" style="left:397px;top:357px"><svg viewBox="0 0 32 32"><circle cx="16" cy="16" r="9" fill="none" stroke="#fff"/><path d="M16 10V16L20 18" stroke="#fff" fill="none"/></svg></div>
    <div class="t svc" style="left:440px;top:316px"><div class="svc-title">Time and Attendance</div><ul><li>Integrated with payroll (no double entry)</li><li>Mobile and geofencing options</li><li>Overtime notices</li><li>Online time-off requests</li><li>Swipe and proximity card clocks</li><li>Biometric clocks</li><li>PTO tracking</li></ul></div>

    <div class="icon" style="left:561px;top:357px"><svg viewBox="0 0 32 32"><path d="M16 8V24M11 24H21M9 11H23M9 11L6 18H12ZM23 11L20 18H26Z" stroke="#fff" fill="none"/></svg></div>
    <div class="t svc" style="left:598px;top:316px"><div class="svc-title">Compliance</div><ul><li>Certified experts ensure compliance with all labor laws and regulations</li><li>OSHA Reporting</li><li>Affirmative Action (EEOC)</li><li>Affordable Care Act (ACA)</li><li>Family Medical Leave Act (FMLA)</li><li>Workers' Comp audits</li></ul></div>

    <div class="icon" style="left:397px;top:429px"><svg viewBox="0 0 32 32"><circle cx="14" cy="14" r="5" fill="none" stroke="#fff"/><path d="M18 18L24 24" stroke="#fff" stroke-width="1.5"/></svg></div>
    <div class="t svc" style="left:440px;top:396px"><div class="svc-title">Talent Acquisition</div><ul><li>Custom careers page</li><li>Standard or custom job applications</li><li style="width:150px">Easy conversion of applicant data to employee data</li><li>Review, rate, and contact applicants</li><li>Mobile-friendly access</li><li>Easy posting to top job boards</li><li>Candidate screening</li></ul></div>

    <div class="t h-section" style="left:753px;top:22px;font-size:14px">WHAT SETS US APART?</div>

    <div class="perk-icon" style="left:753px;top:50px"><svg viewBox="0 0 32 32"><g fill="#fff"><circle cx="9" cy="11" r="2"/><circle cx="16" cy="11" r="2"/><circle cx="23" cy="11" r="2"/><rect x="7.5" y="14" width="3" height="9"/><rect x="14.5" y="14" width="3" height="9"/><rect x="21.5" y="14" width="3" height="9"/></g></svg></div>
    <div class="t perk" style="left:753px;top:93px">Our dedicated team of experts is always just a call or email away! You get direct phone numbers to the professionals you need!</div>
    <div class="perk-icon" style="left:865px;top:50px"><svg viewBox="0 0 32 32"><path d="M6 14L16 9 26 14 16 19Z" fill="#fff"/><path d="M11 17V21Q16 24 21 21V17" fill="#fff"/></svg></div>
    <div class="t perk" style="left:865px;top:93px">We are equipped with education, experience, certifications, and motivation. Our staff executes at the highest level in payroll and HR every day.</div>
    <div class="perk-icon" style="left:977px;top:50px"><svg viewBox="0 0 32 32"><circle cx="11" cy="16" r="3.5" fill="#fff"/><circle cx="22" cy="10" r="2.5" fill="none" stroke="#fff"/><circle cx="22" cy="22" r="2.5" fill="none" stroke="#fff"/><path d="M14 14.5L20 11M14 17.5L20 21" stroke="#fff"/></svg></div>
    <div class="t perk" style="left:977px;top:93px">Employee information is automatically integrated across all modules, eliminating duplicate data entry and significantly reducing errors.</div>

    <div class="perk-icon" style="left:753px;top:138px"><svg viewBox="0 0 32 32"><rect x="6" y="10" width="14" height="10" fill="none" stroke="#fff" stroke-width="1.5"/><path d="M10 24H16M13 20V24" stroke="#fff"/><rect x="22" y="9" width="5" height="15" fill="#fff"/></svg></div>
    <div class="t perk" style="left:753px;top:180px">Our advanced software is used to process payroll for over 88,000 companies and 2.2 million employees nation-wide. It makes even the most complex payrolls easy.</div>
    <div class="perk-icon" style="left:865px;top:138px"><svg viewBox="0 0 32 32"><path d="M10 7H19L23 11V25H10Z" fill="none" stroke="#fff" stroke-width="1.3"/><path d="M13 14H20M13 17H20M13 20H20" stroke="#fff"/></svg></div>
    <div class="t perk" style="left:865px;top:180px">Access your employee information how you need it when you need it with our quick-access reports and intuitive report writer. We even provide custom reports!</div>
    <div class="perk-icon" style="left:977px;top:138px"><svg viewBox="0 0 32 32"><path d="M15 13A4 4 0 0 1 23 12 3 3 0 0 1 24 18H15A2.5 2.5 0 0 1 15 13Z" fill="none" stroke="#fff"/><rect x="6" y="16" width="10" height="7" fill="none" stroke="#fff"/><path d="M9 26H13" stroke="#fff"/></svg></div>
    <div class="t perk" style="left:977px;top:180px">Our client branded, cloud-based Employee and Manager portals allow your employees to access their payroll information quicker and more securely than ever before!</div>

    <div class="t brand brand--compact" style="left:776px;top:252px"><i></i>BRIGHTLANE STAFFWORKS</div>
    <div class="t pill" style="left:934px;top:245px">SAVE TIME AND STAY FOCUSED ON RUNNING YOUR BUSINESS</div>
  </section>

</div>
</body>
</html>
```